Investment Business - Biz Card Design

Using the attached logo files, please create a superior business card design for Brantwell Holdings.

The "back" of the card should feature the logo (either in colour, or white/black over a feature colour)

The "front" of the card should feature: name, email, and phone

The design should be minimal and clean.

Target Market(s)

Business owners who need our investment services.

Industry/Entity Type

Business

```html
<!DOCTYPE html>
<html lang="en">
<head>
<meta charset="utf-8">
<title>Brantwell Holdings – Business Cards</title>
<link rel="stylesheet" href="https://fonts.googleapis.com/css2?family=Questrial&family=Arimo:wght@400&display=swap">
<style>
  :root {
    --backdrop: #d4d4d4;
    --card-dark: #1f1a18;
    --card-light: #ffffff;
    --navy: #2b2f86;
    --sky: #2a9be0;
    --ink: #1c1c1c;
    --white: #ffffff;
  }
  * { margin: 0; padding: 0; box-sizing: border-box; }
  html, body { width: 1200px; height: 944px; overflow: hidden; }
  body {
    background: var(--backdrop);
    position: relative;
    font-family: "Arimo", Arial, sans-serif;
  }
  .card {
    position: absolute;
    width: 600px;
    height: 344px;
    border-radius: 30px;
    box-shadow: 0 10px 26px rgba(0,0,0,0.28);
  }
  .card-back {
    left: 110px; top: 120px;
    background: var(--card-dark);
  }
  .card-front {
    left: 490px; top: 470px;
    background: var(--card-light);
  }
  .wordmark {
    font-family: "Questrial", "Century Gothic", sans-serif;
    text-transform: uppercase;
    letter-spacing: 3px;
    line-height: 1;
    white-space: nowrap;
  }
  .card-back .wordmark {
    position: absolute;
    left: 0; right: 0; top: 118px;
    text-align: center;
    color: var(--white);
    font-size: 40px;
  }
  .card-back .website {
    position: absolute;
    left: 0; right: 0; top: 262px;
    text-align: center;
    color: var(--white);
    font-size: 17px;
    letter-spacing: 1.5px;
  }
  .card-front .wordmark {
    position: absolute;
    left: 44px; top: 52px;
    color: var(--navy);
    font-size: 32px;
  }
  .divider {
    position: absolute;
    left: 24px; right: 30px; top: 176px;
    height: 2px;
    background: var(--sky);
  }
  .holder {
    position: absolute;
    right: 40px; top: 150px;
    text-align: right;
  }
  .holder .name {
    color: var(--navy);
    font-size: 20px;
    letter-spacing: 0.5px;
  }
  .holder .role {
    color: var(--ink);
    font-size: 14px;
    margin-top: 8px;
  }
  .contacts {
    position: absolute;
    left: 24px; top: 196px;
    list-style: none;
    color: var(--ink);
    font-size: 17px;
    line-height: 22px;
  }
  .contacts li { display: flex; align-items: center; gap: 8px; }
  .contacts svg { width: 14px; height: 14px; fill: var(--navy); flex: none; }
  .address {
    position: absolute;
    right: 40px; top: 252px;
    text-align: right;
    color: var(--ink);
    font-size: 16px;
    line-height: 21px;
    font-style: normal;
  }
</style>
</head>
<body>
  <section class="card card-back" aria-label="Card back">
    <div class="wordmark">Brantwell Holdings</div>
    <div class="website">www.brantwellhold.com</div>
  </section>

  <section class="card card-front" aria-label="Card front">
    <div class="wordmark">Brantwell Holdings</div>
    <div class="divider"></div>
    <div class="holder">
      <div class="name">Marcus Hale</div>
      <div class="role">director</div>
    </div>
    <ul class="contacts">
      <li>
        <svg viewBox="0 0 16 16" aria-hidden="true"><path d="M4 1l3 3-2 2c1 2 3 4 5 5l2-2 3 3-2 3C7 15 1 9 1 3z"/></svg>
        512-555-0148
      </li>
      <li>
        <svg viewBox="0 0 16 16" aria-hidden="true"><rect x="4" y="1" width="8" height="5"/><rect x="1" y="6" width="14" height="7" rx="1"/><rect x="4" y="11" width="8" height="4"/></svg>
        512-555-0149
      </li>
      <li>
        <svg viewBox="0 0 16 16" aria-hidden="true"><path d="M1 3h14v10H1z M1 3l7 6 7-6" stroke="#fff" stroke-width="1"/></svg>
        info@brantwellhold.com
      </li>
      <li>
        <svg viewBox="0 0 16 16" aria-hidden="true"><circle cx="8" cy="8" r="7"/></svg>
        www.brantwellhold.com
      </li>
    </ul>
    <address class="address">4100 Alder Crest Rd<br>Harlow, TX 78010</address>
  </section>
</body>
</html>
```